Business card - Brio Margin - size 85 mm * 55 mm

We need new business cards. Design must fit with our vision of the firm. You find in the attached file our logo and a short description of our firm (mission, vision, value, business and so on).

Target Market(s)

Consulting firm in performance improvement

Industry/Entity Type

Management Consulting

Contact Information for Business Card

SIZE
85 mm * 55 mm
INFORMATIONS
name surname
role position
telephone number
email address

Requirements
Must have
• the brand must APPEAR for the rest Would we like to have something sleek, inspired to a "just right" approach
Should not have
• Please avoid the black color as background

```html
<!DOCTYPE html>
<html lang="en">
<head>
<meta charset="utf-8">
<title>Brio Margin – Business Cards</title>
<link href="https://fonts.googleapis.com/css2?family=Lato:wght@400;700&display=swap" rel="stylesheet">
<style>
  :root {
    --bg: #212121;
    --brand-green: #9acb3c;
    --faint-green: #8fc038;
    --paper: #ffffff;
    --ink: #4a4a4a;
    --wave-grey: #646262;
    --ghost-green: #f1f7e8;
  }
  * { margin: 0; padding: 0; box-sizing: border-box; }
  html, body { width: 1189px; height: 1200px; overflow: hidden; background: var(--bg); }
  body { position: relative; font-family: "Lato", Arial, sans-serif; }

  .card {
    position: absolute;
    left: 221px;
    width: 756px;
    height: 488px;
    overflow: hidden;
    box-shadow: 6px 8px 14px rgba(0,0,0,0.55);
  }
  .card--front { top: 67px; background: var(--brand-green); }
  .card--back  { top: 626px; background: var(--paper); }

  .card svg.decor { position: absolute; inset: 0; }

  .brand-name {
    position: absolute;
    font-weight: 700;
    line-height: 1;
    text-transform: uppercase;
    white-space: nowrap;
  }
  .card--front .brand-name {
    color: var(--paper);
    left: 0; width: 756px;
    text-align: center;
    top: 330px;
    font-size: 28px;
    letter-spacing: 16px;
    padding-left: 16px;
  }
  .card--back .brand-name {
    color: var(--brand-green);
    left: 44px;
    top: 209px;
    font-size: 25px;
    letter-spacing: 13px;
  }

  .contact { position: absolute; left: 424px; top: 193px; color: var(--ink); }
  .contact__name { color: var(--brand-green); font-weight: 700; font-size: 31px; line-height: 1; text-transform: uppercase; }
  .contact__role { font-size: 22px; margin-top: 4px; }
  .contact__list { list-style: none; margin-top: 34px; }
  .contact__item { display: flex; align-items: center; font-size: 22px; height: 28px; }
  .contact__icon { width: 24px; height: 24px; margin-right: 10px; flex: none; }

  .website { position: absolute; left: 423px; top: 433px; color: var(--paper); font-size: 20px; letter-spacing: 0.5px; }
</style>
</head>
<body>

  <section class="card card--front" aria-label="Card front">
    <svg class="decor" width="756" height="488" viewBox="0 0 756 488">
      <circle cx="350" cy="244" r="272" fill="none" stroke="var(--faint-green)" stroke-width="30" opacity="0.55"/>
      <circle class="brand-dot" cx="362" cy="220" r="86" fill="none" stroke="var(--paper)" stroke-width="7"/>
    </svg>
    <div class="brand-name">Brio Margin</div>
  </section>

  <section class="card card--back" aria-label="Card back">
    <svg class="decor" width="756" height="488" viewBox="0 0 756 488">
      <circle cx="600" cy="120" r="165" fill="none" stroke="var(--ghost-green)" stroke-width="26"/>
      <circle class="brand-dot" cx="185" cy="113" r="72" fill="none" stroke="var(--brand-green)" stroke-width="6"/>
      <path class="wave wave--grey" fill="var(--wave-grey)"
        d="M0,326 C80,372 250,382 420,374 C580,367 700,372 752,402 C650,382 500,380 300,392 C180,400 60,410 0,405 Z"/>
      <path class="wave wave--green" fill="var(--brand-green)"
        d="M0,418 C200,436 420,420 756,408 L756,488 L0,488 Z"/>
    </svg>

    <div class="brand-name">Brio Margin</div>

    <div class="contact">
      <div class="contact__name">Lena Ortiz</div>
      <div class="contact__role">Chief Executive Officer</div>
      <ul class="contact__list">
        <li class="contact__item">
          <svg class="contact__icon" viewBox="0 0 24 24" aria-hidden="true">
            <rect width="24" height="24" rx="3" fill="var(--brand-green)"/>
            <path d="M8 5 L10.5 5 L11.5 9 L10 10.5 C10.8 12.5 11.8 13.8 13.5 14.8 L15 13.4 L18.5 14.5 L18.5 17 C18.5 18 17.5 19 16 18.8 C10.5 18 6.5 13.5 6 8.2 C5.9 6.2 6.8 5 8 5 Z" fill="var(--paper)"/>
          </svg>
          555 204 7716
        </li>
        <li class="contact__item">
          <svg class="contact__icon" viewBox="0 0 24 24" aria-hidden="true">
            <rect width="24" height="24" rx="3" fill="var(--brand-green)"/>
            <rect x="5" y="7" width="14" height="10" fill="none" stroke="var(--paper)" stroke-width="1.6"/>
            <path d="M5 7 L12 13 L19 7 M5 17 L10 12 M19 17 L14 12" fill="none" stroke="var(--paper)" stroke-width="1.4"/>
          </svg>
          lena@briomargin.com
        </li>
      </ul>
    </div>

    <div class="website">www.briomargin.com</div>
  </section>

</body>
</html>
```